Business Card Design

We need a business card design for a new company called Riverbend Advisory, LLC. We are a project management and software engineering consulting company. We prefer to use blues but am open to any colors. We would like out design to show strength and creativity.

I've uploaded new logo designs to the project.  Please use these logo designs for the business card. Thanks!

Industry/Entity Type

Software

Contact Information for Business Card

Daniel Whitford
Consultant
Owner

Riverbend Advisory, LLC

2716 5th St. S #4372
Arlington, VA 22198

703-555-0187
dwhitford@rvbadv.example
www.rvbadv.example

```html
<!DOCTYPE html>
<html lang="en">
<head>
<meta charset="utf-8">
<title>Riverbend Advisory – Business Card</title>
<link rel="stylesheet" href="https://fonts.googleapis.com/css2?family=Open+Sans:wght@400;600;700&display=swap">
<style>
  :root {
    --stage: #e9e7e4;
    --card-white: #ffffff;
    --brand-blue: #1d6384;
    --brand-blue-deep: #15506d;
    --brand-blue-light: #2a7396;
    --navy-text: #2b4a5e;
    --body-text: #263845;
    --muted-text: #55707f;
    --accent-red: #d2392f;
    --divider: #5f7f90;
  }
  html, body {
    margin: 0;
    width: 1200px;
    height: 800px;
    overflow: hidden;
    background: var(--stage);
    font-family: "Open Sans", Arial, sans-serif;
  }
  .canvas {
    position: relative;
    width: 1200px;
    height: 800px;
  }

  /* Back of card */
  .card-back {
    position: absolute;
    left: 110px;
    top: 120px;
    width: 320px;
    height: 560px;
    border-radius: 4px;
    overflow: hidden;
    background: var(--brand-blue);
    box-shadow: 0 10px 30px rgba(0,0,0,.18);
  }
  .card-back__texture {
    position: absolute;
    inset: 0;
    background: linear-gradient(180deg, var(--brand-blue-light) 0%, var(--brand-blue) 50%, var(--brand-blue-deep) 100%);
  }
  .card-back__brand {
    position: absolute;
    left: 50%;
    top: 50%;
    transform: translate(-50%, -50%) rotate(90deg);
    white-space: nowrap;
    color: var(--card-white);
    font-weight: 600;
    font-size: 34px;
    letter-spacing: 1px;
  }

  /* Front of card */
  .card-front {
    position: absolute;
    left: 540px;
    top: 240px;
    width: 560px;
    height: 320px;
    border-radius: 4px;
    overflow: hidden;
    background: var(--card-white);
    box-shadow: 0 10px 30px rgba(0,0,0,.18);
  }
  .card-front__brand {
    position: absolute;
    left: 34px;
    top: 34px;
    color: var(--navy-text);
    font-weight: 600;
    font-size: 28px;
    letter-spacing: .5px;
  }
  .person {
    position: absolute;
    left: 34px;
    top: 92px;
  }
  .person__name {
    margin: 0;
    color: var(--accent-red);
    font-weight: 700;
    font-size: 19px;
    text-transform: uppercase;
    letter-spacing: .5px;
  }
  .person__title {
    margin: 2px 0 0;
    color: var(--muted-text);
    font-size: 12px;
  }
  .divider {
    position: absolute;
    left: 236px;
    top: 168px;
    width: 1px;
    height: 92px;
    background: var(--divider);
  }
  .contact {
    position: absolute;
    left: 260px;
    top: 160px;
    color: var(--body-text);
    font-size: 13px;
    line-height: 19px;
  }
  .contact__company {
    color: var(--accent-red);
    font-weight: 700;
  }
  .contact__line {
    display: flex;
    align-items: center;
    gap: 7px;
  }
  .contact__icon {
    width: 13px;
    height: 13px;
    flex: none;
  }
  .web-band {
    position: absolute;
    left: 0;
    bottom: 0;
    width: 100%;
    height: 44px;
    background: var(--brand-blue);
    display: flex;
    align-items: center;
  }
  .web-band__url {
    margin-left: 96px;
    color: var(--card-white);
    font-weight: 600;
    font-size: 14px;
    letter-spacing: 4px;
  }
</style>
</head>
<body>
<main class="canvas">

  <section class="card-back" aria-label="Card back">
    <div class="card-back__texture" role="img" aria-label="Blue background with soft horizontal rounded stripes"></div>
    <div class="card-back__brand">Riverbend Advisory</div>
  </section>

  <section class="card-front" aria-label="Card front">
    <div class="card-front__brand">Riverbend Advisory</div>

    <div class="person">
      <p class="person__name">Daniel Whitford</p>
      <p class="person__title">Consultant Owner</p>
    </div>

    <div class="divider"></div>

    <address class="contact" style="font-style:normal">
      <div class="contact__company">Riverbend Advisory, LLC</div>
      <div>2716 5th St. S #4372</div>
      <div>Arlington, VA 22198</div>
      <div class="contact__line">
        <svg class="contact__icon" viewBox="0 0 13 13" aria-hidden="true">
          <rect width="13" height="13" rx="2" fill="#d2392f"/>
          <rect x="4" y="2.5" width="5" height="8" rx="1" fill="none" stroke="#fff" stroke-width="1.2"/>
          <circle cx="6.5" cy="9" r=".6" fill="#fff"/>
        </svg>
        <span>703-555-0187</span>
      </div>
      <div class="contact__line">
        <svg class="contact__icon" viewBox="0 0 13 13" aria-hidden="true">
          <rect width="13" height="13" rx="2" fill="#d2392f"/>
          <rect x="2.5" y="3.5" width="8" height="6" fill="none" stroke="#fff" stroke-width="1.1"/>
          <path d="M2.5 3.5 L6.5 7 L10.5 3.5" fill="none" stroke="#fff" stroke-width="1.1"/>
        </svg>
        <span>dwhitford@rvbadv.example</span>
      </div>
    </address>

    <div class="web-band">
      <span class="web-band__url">www.rvbadv.example</span>
    </div>
  </section>

</main>
</body>
</html>
```